Word Press Website Design with animated splash page + Coding

Web Site Brief
Domain: www.mervalink.ai
Job:
Word Press Site creative and coding, we have word press hosting through HostPrairie and will grant access to the winning design to implement the site.
Splash page with animation of our current logo.
Approx 7 pages (several are the same layout)
We require the ability to add/update text and pictures to the site ourselves after initial build.
All pages other than splash should have a floating button as a way to connect with us and open to a simple form that allows for contact information and then sends to an email we select.
Background:
After a year of R&D TRB is launching our new ai driven product to market. As such we are also rebranding from www.trbpartners.com to www.mervalink.ai. Our customers are large technology companies and TRB has been in business for the last 20 years.
Site Overview:
We are looking for a fairly simple site with regards to pages but one that brings a look and feel of high tech and new. We are not tied to the more standard website design as we are looking forward not to the past or even today. The initial content will be fairly simple and straight forward mainly made up of pictures with text. Although the content will be fairly simple to start we want some wow factor for the layout and functionality.
Site Specifics:
We recently had a new logo designed and have all color and file type versions available. We have posted a zipped filed with all the PNG files in different colors layouts. We will require a link to our social media LinkedIn, FaceBook, Twitter.
We are including a power point with a basic layout of our site as follows:
Site Layout:
Splash Page:
This will be the first page reached and we would like the "Market Lenses" part of our logo there then animate the first part of our logo. For the animation you can go to this site www.quenvestry.com and see how the red circle builds. Starting with the C then the S and last the G. At the same time we would like the following phrase to build under our logo “Ai Driven Business Insight and Revenue Generation Solutions”. The build should take somewhere around 4 seconds then move to our main page.
Main Page:
The main page will contain 5 links to the next layer of pages.
Layer 1 page type 1: (3 of the 5 pages)
Page type one will have some overall text at the top then we are looking for a two column table with text and then a standardized picture size format. As we will have different size picture to include we would like to keep the grid/table standardized with the same picture size (similar to a thumb nail but not that small) that can then pop out to full size when you hover or click.
Layer 1 page type 2: (2 of the 5 pages)
These two pages will mainly be text but the layout is not yet determined.
We are also including a powerpoint deck with more information on each of the 5 subpages. Most contain pictures you can use for the layout design of the 3 subpages that have pictures embedded.
We will be judging look and feel for the splash page, the main page, and the two types of sub pages. Once we select the winner credentials will be granted to use your design to build out the page in Wordpress on our current hosting site.
We would like to find a designer we can continue to work with as we develop the site further.
thanks

```html
<!DOCTYPE html>
<html lang="en">
<head>
<meta charset="utf-8">
<title>TRB Market Lenses</title>
<link rel="stylesheet" href="https://fonts.googleapis.com/css2?family=Share+Tech+Mono&family=Montserrat:wght@700&display=swap">
<style>
  :root {
    --ink: #ffffff;
    --accent: #22b8e8;
    --bg-deep: #131313;
    --bg-mid: #2a2a2a;
    --bg-light: #4a4a4a;
    --ring: #8a8a8a;
    --dot: #6d6d6d;
  }
  * { margin: 0; padding: 0; box-sizing: border-box; }
  html, body { width: 1200px; height: 673px; overflow: hidden; background: var(--bg-deep); }
  .page {
    position: relative;
    width: 1200px;
    height: 673px;
    overflow: hidden;
    font-family: "Share Tech Mono", monospace;
    color: var(--ink);
  }
  .sky {
    position: absolute;
    inset: 0;
    background:
      radial-gradient(ellipse 260px 150px at 560px 90px, rgba(110,110,110,0.55), transparent 70%),
      radial-gradient(ellipse 420px 200px at 300px 150px, rgba(60,60,60,0.6), transparent 75%),
      radial-gradient(ellipse 380px 220px at 880px 300px, rgba(70,70,70,0.5), transparent 75%),
      linear-gradient(180deg, var(--bg-mid) 0%, #222 45%, var(--bg-deep) 80%);
  }
  .brand {
    position: absolute;
    left: 45px;
    top: 43px;
    height: 44px;
    display: flex;
    align-items: center;
    gap: 11px;
  }
  .brand-mark {
    width: 42px;
    height: 42px;
    border-radius: 50%;
    border: 3px solid var(--ink);
  }
  .brand-name {
    font-family: "Share Tech Mono", monospace;
    font-size: 19px;
    letter-spacing: 1px;
    color: var(--ink);
  }
  .contact-link {
    position: absolute;
    right: 44px;
    top: 57px;
    font-size: 13px;
    letter-spacing: 1.2px;
    color: var(--ink);
    text-decoration: none;
  }
  .headline {
    position: absolute;
    left: 175px;
    top: 309px;
    font-size: 40px;
    font-weight: 400;
    line-height: 45px;
    letter-spacing: 3.4px;
  }
  .headline .highlight { color: var(--accent); }
  .read-on {
    position: absolute;
    left: 378px;
    top: 432px;
    width: 152px;
    height: 18px;
    text-decoration: none;
    color: var(--ink);
  }
  .read-on .rule {
    position: absolute;
    left: 0;
    right: 0;
    top: 9px;
    height: 1px;
    background: var(--accent);
  }
  .read-on .label {
    position: absolute;
    right: 0;
    top: 0;
    font-size: 13px;
    letter-spacing: 0.6px;
    line-height: 18px;
  }
  .float-button {
    position: absolute;
    left: 1088px;
    top: 346px;
    width: 69px;
    height: 69px;
  }
</style>
</head>
<body>
<main class="page">
  <div class="sky" role="img" aria-label="Dark, moody storm clouds filling the background"></div>

  <header>
    <a class="brand" href="#">
      <span class="brand-mark"></span>
      <span class="brand-name">MARKET LENSES</span>
    </a>
    <a class="contact-link" href="#">Contact us</a>
  </header>

  <h1 class="headline">What is <span class="highlight">TRB Market</span><br><span class="highlight-none">Lenses?</span></h1>

  <a class="read-on" href="#">
    <span class="rule"></span>
    <span class="label">read on</span>
  </a>

  <svg class="float-button" viewBox="0 0 69 69" aria-label="Connect with us">
    <circle cx="34.5" cy="34.5" r="32.5" fill="none" stroke="var(--ring)" stroke-width="2.5"/>
    <circle cx="34.5" cy="34.5" r="19" fill="none" stroke="var(--ring)" stroke-width="2.5"/>
    <circle cx="34.5" cy="34.5" r="15.5" fill="var(--dot)"/>
  </svg>
</main>
</body>
</html>
```